Awesome Business Card Design needed!

Hey there.
I'm looking for a simple but awesome business card design.
Type of company: Online advertisement agency
(please don't use the typical business people or statistics images on the card)
The front has to display the business name
and possibly some sort of logo ( perhaps something with the two M's of the biz name )
And the back of the card should say:
Name
Phone
Email
Let your imagination flow.
here are some designs that I like and that you can use as inspiration.
Simple but Awesome
http://images.pixelvantor.net/designs/55128_877673_43091_thumbnail.jpg
http://images.pixelvantor.net/designs/37714_747642_40106_image.jpg
http://images.pixelvantor.net/designs/55128_877673_43091_image.jpg
http://images.pixelvantor.net/designs/51321_781878_43091_image.jpg
http://images.pixelvantor.net/designs/33378_399063_15912_image.jpg
http://images.pixelvantor.net/designs/2337_271604_9495_image.jpg
good luck

```html
<!DOCTYPE html>
<html lang="en">
<head>
<meta charset="utf-8">
<title>Norvale Media – Business Card</title>
<link rel="stylesheet" href="https://fonts.googleapis.com/css2?family=Josefin+Sans:wght@300&family=Open+Sans:wght@400;700&display=swap">
<style>
  :root {
    --canvas-bg: #eef0f1;
    --card-black: #050505;
    --card-swoop: #1a1819;
    --card-swoop-light: #2a2627;
    --gold: #c99a3e;
    --gold-light: #e6bf7a;
    --blush: #f3dcd5;
    --ice: #eaf6fb;
    --ice-mid: #bcd6e4;
    --slate: #6f8494;
    --slate-dark: #2c2e35;
    --band: #f4f9fb;
    --ink: #1b1d22;
    --white: #ffffff;
  }
  * { margin: 0; padding: 0; box-sizing: border-box; }
  html, body {
    width: 1200px;
    height: 621px;
    overflow: hidden;
    background: var(--canvas-bg);
  }
  .stage {
    position: relative;
    width: 1200px;
    height: 621px;
  }
  .card {
    position: absolute;
    top: 268px;
    width: 488px;
    height: 282px;
    border-radius: 30px;
    overflow: hidden;
  }
  .card svg { position: absolute; inset: 0; }

  /* Front */
  .card--front { left: 75px; background: var(--card-black); }
  .front-bar {
    position: absolute;
    left: 0; top: 129px;
    width: 65px; height: 26px;
    background: linear-gradient(90deg, #8a6a34, var(--gold-light));
  }
  .front-chip {
    position: absolute;
    left: 65px; top: 129px;
    width: 20px; height: 26px;
    background: var(--blush);
  }
  .front-name {
    position: absolute;
    left: 86px; top: 124px;
    font-family: "Josefin Sans", sans-serif;
    font-weight: 300;
    font-size: 31px;
    letter-spacing: 2px;
    color: var(--gold-light);
    white-space: nowrap;
  }
  .front-mark {
    position: absolute;
    left: 388px; top: 100px;
    width: 84px; height: 84px;
    border: 2px solid var(--gold);
    border-radius: 50%;
  }

  /* Back */
  .card--back {
    left: 641px;
    background:
      radial-gradient(ellipse 70% 110% at 25% 35%, var(--ice) 0%, var(--ice-mid) 45%, var(--slate) 78%, var(--slate-dark) 100%);
  }
  .back-band {
    position: absolute;
    left: 110px; top: 50px;
    width: 378px; height: 35px;
    background: var(--band);
  }
  .back-mark {
    position: absolute;
    left: 29px; top: 14px;
    width: 96px; height: 96px;
    border-radius: 50%;
    background: var(--card-black);
  }
  .back-name {
    position: absolute;
    left: 127px; top: 52px;
    font-family: "Josefin Sans", sans-serif;
    font-weight: 300;
    font-size: 29px;
    letter-spacing: 2px;
    color: var(--ink);
    white-space: nowrap;
  }
  .contact {
    position: absolute;
    left: 58px; top: 120px;
    list-style: none;
    font-family: "Open Sans", sans-serif;
    font-size: 15px;
    color: var(--ink);
    letter-spacing: 0.8px;
  }
  .contact li {
    display: flex;
    align-items: center;
    height: 27px;
  }
  .contact .label {
    width: 56px;
    display: flex;
    align-items: center;
  }
  .contact .label-n { font-weight: 700; font-size: 16px; padding-left: 4px; }
</style>
</head>
<body>
<main class="stage">

  <section class="card card--front" aria-label="Card front">
    <svg width="488" height="282" viewBox="0 0 488 282" aria-hidden="true">
      <path d="M0 90 C120 110 260 150 488 120 L488 282 L0 282 Z" fill="var(--card-swoop)"/>
      <path d="M0 190 C150 150 300 160 488 220 L488 282 L0 282 Z" fill="var(--card-black)"/>
      <path d="M380 0 C440 40 470 90 488 150 L488 0 Z" fill="var(--card-swoop-light)"/>
    </svg>
    <div class="front-bar"></div>
    <div class="front-chip"></div>
    <div class="front-name">NORVALE Media</div>
    <div class="front-mark"></div>
  </section>

  <section class="card card--back" aria-label="Card back">
    <svg width="488" height="282" viewBox="0 0 488 282" aria-hidden="true">
      <path d="M20 0 C-10 110 40 230 140 282" fill="none" stroke="var(--white)" stroke-opacity="0.6" stroke-width="2"/>
      <path d="M400 0 C440 30 470 60 488 80 L488 0 Z" fill="var(--slate-dark)"/>
    </svg>
    <div class="back-band"></div>
    <div class="back-mark"></div>
    <div class="back-name">NORVALE Media</div>
    <ul class="contact">
      <li><span class="label label-n">N.</span><span>Norvale Media</span></li>
      <li>
        <span class="label">
          <svg width="26" height="22" viewBox="0 0 26 22" aria-label="Phone">
            <path d="M3 8 C3 3 23 3 23 8 L23 11 L17 11 L17 8 C14 7 12 7 9 8 L9 11 L3 11 Z" fill="var(--ink)"/>
            <path d="M6 12 L20 12 L22 20 L4 20 Z" fill="var(--ink)" transform="rotate(-25 13 15) scale(0)"/>
          </svg>
        </span>
        <span>(054) 555 017</span>
      </li>
      <li>
        <span class="label">
          <svg width="26" height="22" viewBox="0 0 26 22" aria-label="Email">
            <path d="M1 7 L13 1 L25 7 L25 20 L1 20 Z" fill="none" stroke="var(--ink)" stroke-width="1.6"/>
            <path d="M1 7 L13 14 L25 7" fill="none" stroke="var(--ink)" stroke-width="1.6"/>
            <path d="M15 13 L22 20 L18 20 L19 22 Z" fill="var(--ink)"/>
          </svg>
        </span>
        <span>norvalemedia@mailhub.net</span>
      </li>
    </ul>
  </section>

</main>
</body>
</html>
```